Gin Bottle label design

A label for three Gins, 1 Apple flavoured, 1 Bilberry flavoured and one London Dry Gin. All need to incorporate the business logo that i've attached along with the bottle we intend to use. The gin is 40% and will be in a 70cl bottle

```html
<!DOCTYPE html>
<html lang="en">
<head>
<meta charset="utf-8">
<title>Apple Gin Label</title>
<link rel="stylesheet" href="https://fonts.googleapis.com/css2?family=Playfair+Display:wght@700;900&display=swap">
<style>
  :root {
    --canvas-bg: #f4f3f1;
    --burgundy: #6b1c27;
    --burgundy-deep: #561420;
    --gold-light: #e6c877;
    --gold: #c49a43;
    --gold-dark: #9c7328;
    --cream: #ffffff;
    --blush: #c9a3a8;
  }
  * { margin: 0; padding: 0; box-sizing: border-box; }
  html, body {
    width: 840px;
    height: 1200px;
    overflow: hidden;
    background: var(--canvas-bg);
  }
  .canvas {
    position: relative;
    width: 840px;
    height: 1200px;
  }
  .label {
    position: absolute;
    left: 40px;
    top: 97px;
    width: 760px;
    height: 1006px;
    background: var(--burgundy);
    overflow: hidden;
    font-family: "Playfair Display", Georgia, serif;
    box-shadow: 0 6px 24px rgba(0,0,0,0.12);
  }
  .gold-band {
    position: absolute;
    left: 0;
    width: 100%;
    height: 50px;
    background: linear-gradient(90deg, var(--gold-dark), var(--gold-light) 30%, var(--gold) 55%, var(--gold-light) 80%, var(--gold-dark));
  }
  .gold-band--top { top: 0; }
  .gold-band--bottom { bottom: 0; }
  .orchard-art {
    position: absolute;
    left: 0;
    top: 0;
    width: 100%;
    height: 580px;
  }
  .brand-seal {
    position: absolute;
    left: 202px;
    top: 159px;
    width: 350px;
    height: 350px;
    border-radius: 50%;
    background: var(--cream);
    display: flex;
    align-items: center;
    justify-content: center;
    text-align: center;
  }
  .brand-name {
    color: var(--burgundy);
    font-weight: 700;
    font-size: 46px;
    line-height: 1.05;
    letter-spacing: 1px;
  }
  .product-name {
    position: absolute;
    left: 0;
    width: 100%;
    top: 575px;
    text-align: center;
    color: var(--cream);
    font-weight: 900;
    font-size: 250px;
    line-height: 1;
    letter-spacing: -4px;
  }
  .flavour {
    position: absolute;
    left: 0;
    width: 100%;
    top: 790px;
    text-align: center;
    color: var(--gold);
    font-weight: 700;
    font-size: 64px;
    letter-spacing: 44px;
    padding-left: 44px;
  }
  .spec {
    position: absolute;
    top: 892px;
    color: var(--cream);
    font-weight: 700;
    font-size: 28px;
  }
  .spec--abv { left: 53px; }
  .spec--volume { right: 46px; }
</style>
</head>
<body>
<main class="canvas">
  <section class="label">
    <div class="gold-band gold-band--top"></div>

    <svg class="orchard-art" viewBox="0 0 760 580" role="img" aria-label="Engraved illustration of apples, apple halves and leaves on branches">
      <defs>
        <radialGradient id="orchardTone" cx="50%" cy="40%" r="70%">
          <stop offset="0%" stop-color="#a86a72" stop-opacity="0.55"/>
          <stop offset="60%" stop-color="#8a3c47" stop-opacity="0.45"/>
          <stop offset="100%" stop-color="#6b1c27" stop-opacity="0"/>
        </radialGradient>
      </defs>
      <rect x="0" y="0" width="760" height="580" fill="url(#orchardTone)"/>
    </svg>

    <div class="brand-seal">
      <p class="brand-name">The Olive<br>Table</p>
    </div>

    <h1 class="product-name">GIN</h1>
    <p class="flavour">APPLE</p>

    <p class="spec spec--abv">40% VOL</p>
    <p class="spec spec--volume">70cl</p>

    <div class="gold-band gold-band--bottom"></div>
  </section>
</main>
</body>
</html>
```